Need a book cover design for book titled: Rising Through the Glow--Simple Keys for the Awakening

This book describes and presents tools to connect with and activate the Lightbody that we all carry within us. It talks about the Lighbody, brief history, lightbody levels and offers exercises to bring light into the body.
I envision a design that shows a physical body changing into light /surrounded by light; a resurrected body ascending to higher dimensions of Spirit o anything comparable .

Need extra days to review

Need extra days to review

Target Market(s)

Mature audience of spiritual seekers and those on spiritual path

Requirements
Must have
• Space on backcover for book summary at top and title and author name on spine.

```html
<!DOCTYPE html>
<html lang="en">
<head>
<meta charset="utf-8">
<title>Rising Through the Glow — Cover Wrap</title>
<link rel="stylesheet" href="https://fonts.googleapis.com/css2?family=Cinzel:wght@400;600&family=Open+Sans:wght@600&display=swap">
<style>
  :root {
    --space-deep: #1a1470;
    --space-blue: #2a3bc4;
    --nebula-violet: #7a2bc0;
    --nebula-magenta: #d43fb8;
    --nebula-pink: #f28ad8;
    --glow-white: #ffffff;
    --ink: #ffffff;
    --halo: rgba(255, 230, 255, 0.85);
  }
  * { margin: 0; padding: 0; box-sizing: border-box; }
  html, body { width: 1200px; height: 836px; overflow: hidden; background: var(--space-deep); }
  .cover-wrap { position: relative; width: 1200px; height: 836px; overflow: hidden; color: var(--ink); }

  .cosmic-backdrop {
    position: absolute; inset: 0;
    background:
      radial-gradient(ellipse 150px 260px at 926px 440px, var(--glow-white) 0%, rgba(255,255,255,0.9) 30%, rgba(255,180,240,0.55) 55%, rgba(255,140,230,0) 100%),
      radial-gradient(ellipse 330px 420px at 926px 400px, rgba(242,138,216,0.75) 0%, rgba(212,63,184,0.35) 55%, rgba(212,63,184,0) 100%),
      radial-gradient(ellipse 420px 300px at 260px 180px, rgba(212,63,184,0.7) 0%, rgba(122,43,192,0.3) 60%, rgba(122,43,192,0) 100%),
      radial-gradient(ellipse 380px 260px at 330px 430px, rgba(190,70,200,0.55) 0%, rgba(190,70,200,0) 100%),
      radial-gradient(ellipse 500px 260px at 300px 720px, rgba(40,70,220,0.8) 0%, rgba(40,70,220,0) 100%),
      radial-gradient(ellipse 360px 240px at 1100px 720px, rgba(30,60,200,0.7) 0%, rgba(30,60,200,0) 100%),
      linear-gradient(160deg, var(--nebula-violet) 0%, var(--space-blue) 45%, var(--nebula-violet) 70%, var(--space-deep) 100%);
  }

  .serif-caps { font-family: "Cinzel", "Copperplate", serif; font-weight: 600; text-transform: uppercase; text-shadow: 0 0 10px var(--halo), 0 0 3px var(--halo); }

  /* Back cover */
  .back-title { position: absolute; left: 22px; top: 62px; font-size: 31px; letter-spacing: 0.5px; white-space: nowrap; }
  .back-summary, .author-bio {
    position: absolute; left: 21px; width: 500px;
    font-family: "Open Sans", "Segoe UI", sans-serif; font-weight: 600;
    font-size: 12.6px; line-height: 15.3px; text-align: justify;
    text-shadow: 0 0 2px rgba(40,0,80,0.6);
  }
  .back-summary { top: 164px; }
  .about-heading { position: absolute; left: 21px; width: 500px; top: 465px; text-align: center; font-family: "Cinzel", serif; font-weight: 400; font-size: 23px; text-transform: uppercase; text-shadow: 0 0 6px var(--halo); }
  .author-bio { top: 527px; left: 23px; }
  .isbn-box { position: absolute; left: 392px; top: 731px; width: 151px; height: 67px; background: var(--glow-white); }

  /* Spine */
  .spine-title, .spine-author {
    position: absolute; left: 589px; writing-mode: vertical-rl;
    font-family: "Cinzel", serif; font-weight: 400; font-size: 13.5px; text-transform: uppercase; white-space: nowrap;
    text-shadow: 0 0 4px var(--halo);
  }
  .spine-title { top: 22px; }
  .spine-author { top: 660px; }

  /* Front cover */
  .front-title { position: absolute; left: 676px; top: 56px; width: 514px; font-size: 49px; line-height: 62px; }
  .front-title .line { display: block; white-space: nowrap; }
  .front-title .line-two { text-align: right; }
  .front-subtitle { position: absolute; left: 660px; width: 512px; top: 686px; text-align: center; font-family: "Cinzel", serif; font-weight: 400; font-size: 36px; line-height: 42px; text-transform: uppercase; text-shadow: 0 0 8px var(--halo); }
  .front-author { position: absolute; left: 660px; width: 512px; top: 786px; text-align: center; font-family: "Cinzel", serif; font-weight: 600; font-size: 20px; text-transform: uppercase; text-shadow: 0 0 6px var(--halo); }
</style>
</head>
<body>
<main class="cover-wrap">
  <div class="cosmic-backdrop" role="img" aria-label="Wraparound cosmic nebula in violet, magenta and blue with a glowing human figure of pure light radiating rays on the front cover"></div>

  <section class="back-cover">
    <h2 class="back-title serif-caps">Rising Through the Glow</h2>
    <p class="back-summary">Lorem Ipsum is simply dummy text of the printing and typesetting industry. Lorem Ipsum has been the industry's standard dummy text ever since the 1500s, when an unknown printer took a galley of type and scrambled it to make a type specimen book. It has survived not only five centuries, but also the leap into electronic typesetting, remaining essentially unchanged. It was popularised in the 1960s with the release of Lettrafix sheets containing Lorem Ipsum passages, and more recently with desktop publishing software like Alder PageSmith including versions of Lorem Ipsum. Lorem Ipsum is simply dummy text of the printing and typesetting industry. Lorem Ipsum has been the industry's standard dummy text ever since the 1500s, when an unknown printer took a galley of type and scrambled it to make a type specimen book. It has survived not only five centuries, but also the leap into electronic typesetting, remaining essentially unchanged. It was popularised in the 1960s with the release of Lettrafix sheets containing Lorem Ipsum passages, and more recently with desktop publishing software like Alder PageSmith including versions of Lorem Ipsum.</p>
    <h3 class="about-heading">About the Author</h3>
    <p class="author-bio">Lorem Ipsum is simply dummy text of the printing and typesetting industry. Lorem Ipsum has been the industry's standard dummy text ever since the 1500s, when an unknown printer took a galley of type and scrambled it to make a type specimen book. It has survived not only five centuries, but also the leap into electronic typesetting, remaining essentially unchanged. It was popularised in the 1960s with the release of Lettrafix sheets containing Lorem Ipsum passages, and more recently with desktop publishing software</p>
    <div class="isbn-box"></div>
  </section>

  <section class="spine">
    <span class="spine-title">Rising Through the Glow–Simple Keys for the Awakening</span>
    <span class="spine-author">By Author Name</span>
  </section>

  <section class="front-cover">
    <h1 class="front-title serif-caps">
      <span class="line line-one">Rising Through</span>
      <span class="line line-two">the Glow</span>
    </h1>
    <p class="front-subtitle">Simple Keys for<br>the Awakening</p>
    <p class="front-author">By&nbsp; Author Name</p>
  </section>
</main>
</body>
</html>
```